Norwegian psychologist service needs a fresh and exiting web site*

Norwegian psychologist service: working with therapy, personal development, mastery and personal growth. Focus: children and teenagers with special needs; family dynamics; group processes; individuals with a need for therapy and personal growth. (Our company name: Fjordlys og samhold (means Mastery and Growth).

We already have a logo for the company, which will be used (will be attached in the project).

The webside is to be structured in 4 pages with roll down curtain menus (the numbers are just for guiding the designer - the should not be added):

Page 1: Om Fjordlys og Samhold (about Mastery and Growth): this is where our business is is presented/described shortly: Lorem Ipsum dolor cit...

Page 2: Tjenester (Services): this is where our 5 service areas are presented:
2.1 Utredning (Investigation, diagnosing): Lorem Ipsum dolor cit...
2.2 Rådgivning (consulting): Lorem Ipsum dolor cit...

2.3 Kurs og work shops (courses and work shops): Lorem Ipsum dolor cit...
2.3a Fjordlys og samhold Tema 1 (T1)
2.3b Fjordlys og samhold Tema 2 (T2)
2.3c Fjordlys og samhold Tema 3 (T3)

2.4 Terapi og utvikling (Therapy and development)
2.4a Fjordlys og samhold for individer (FS1)
2.4b Fjordlys og samhold i familier (FS2)
2.4c Fjordlys og samhold i grupper (FS3)
2.4d Fjordlys og samhold i institusjoner (FS4)

Page 3: Aktuelt (Blog): this is our blog where we share knowledge and articles

Page 4: Kontakt (Contact): This is the contact form page. Contact form should constitute:
- Ditt navn (your name)
- E-post (your e-mail)
- Emne (subject)
- Melding (message/description)

Our project should also include suggestion for handheld units (iPhone, iPad).
Updates

We have both been traveling with work for a while, and then unfortunately both of us got sick on return, so we need a few more days to evaluate and choose design. Kind Regards Arvid & Margit

Target Market(s)

Focus on therapy, learning, mastery and growth for children and teenagers with special needs, within the family dynamics, or in a group setting.
OUR MARKETS:
Private market: individuals, families, groups and health industry institutions (with focus on learning, mastery, growth (as well as growing up) and psychiatry for children and teenagers with special difficulties and needs)
Public institutions: Government institutions, state institutions and municipality institutions (e.g. schools, municipality health service, hospitals) that serve the public (families with children and teenagers with special needs, and where learning, mastery, growth (as well as growing up) and potential psychiatry is an issue).

Number of Pages Required

4 page

Font styles to use
Sans Serif

Colors

Designer to choose colors to be used in the design.

Requirements
Must have
• The website must have 4 pages with roll down curtain menus (we have added a PDF with suggested structure, and headings, with sub menus - see attached PDF drawing.
• The web page must also use the added logo file - and make the web page work well with our logo.
• We would like the website to have a modern look and we would like the site to be associated with typical HIGH END TOP QUALITY private health institutions, but with a stronger focus on human beings (hands, faces etc), and not white coats and doctors. We are psychologists in the private market.
• For instance, if photos are being used - we tend to like "warm" almost art-like, "grainy" two-tone (e.g. sepia) photos to illustrate our focus. If designer can find such photos as part of design, it would be interesting to us. We would like a few photos like that integrated in the design.
• We also want a design suggestion for how the web page should look like and behave on handheld units (e.g. iPhone, iPad).
Nice to have
• If designer could find a number of suitable photos that matches the business idea and design requirements (see description above), that could follow website, that would be good.
• It could also be nice to have graphic symbols that denote the different pages/subpages (subjects)....
• HORSES: we sometimes use horses as a "tool" in therapy sessions. The horse is not necessarily used for riding, but for contact, communication and grooming. PHOTOS: we would like the designer to find an opportunity for using a photo reflecting this cooperation between therapist, child, teenager and horse. It is a bit up to the designer to find a way to do this... Since the horse is only a tool, among many other tools, it does not have to be much - but we want to try and see how it will work with a photo that also reflects this part of our business.

```html
<!DOCTYPE html>
<html lang="no">
<head>
<meta charset="utf-8">
<title>Fjordlys og Samhold</title>
<link rel="stylesheet" href="https://fonts.googleapis.com/css2?family=Fira+Sans:wght@500;600;700&family=Source+Sans+3:wght@400;600;700&display=swap">
<style>
:root{
  --blue:#27358f;
  --green:#0f6e36;
  --green-light:#3cae67;
  --ink:#262626;
  --muted:#555;
  --mist:#f0eced;
  --night:#2a2a2a;
  --white:#fff;
}
*{box-sizing:border-box;margin:0;padding:0}
html,body{width:1200px;height:3129px;overflow:hidden;background:var(--white)}
body{font-family:"Source Sans 3",sans-serif;color:var(--ink)}
.page{position:relative;width:1200px;height:3129px;overflow:hidden}
.abs{position:absolute}
.heading{font-family:"Fira Sans",sans-serif;font-weight:600;color:var(--ink);line-height:1}
.rule{display:inline-block;height:1px;background:var(--ink);vertical-align:middle}

/* header */
.topbar{left:711px;top:0;width:489px;height:39px;background:var(--blue);clip-path:polygon(0 0,100% 0,100% 100%,38px 100%);color:var(--white);font-size:12.5px;display:flex;align-items:center;gap:18px;padding-left:52px}
.topbar span{display:flex;align-items:center;gap:5px}
.brand{left:94px;top:22px;display:flex;align-items:center;gap:8px;font-family:"Source Sans 3",sans-serif;font-weight:600;font-size:17px;color:var(--blue);letter-spacing:.5px}
.brand i{width:14px;height:14px;border-radius:50%;background:var(--blue);display:block}
.nav{top:66px;left:711px;display:flex;font-size:13px;font-weight:600}
.nav a{color:var(--ink);text-decoration:none;position:absolute;white-space:nowrap}
.header-line{left:0;top:93px;width:1200px;height:1px;background:#e4e4e4}

/* hero */
.hero-title{left:706px;top:517px;color:var(--white)}
.hero-title .kicker{font-family:"Fira Sans",sans-serif;font-weight:500;font-size:29px;display:flex;align-items:center;gap:10px;margin-left:6px}
.hero-title .kicker .rule{width:62px;background:rgba(255,255,255,.7)}
.hero-title .line1{font-family:"Fira Sans",sans-serif;font-weight:600;font-size:55px;line-height:1;margin-top:6px}
.hero-title .line2{font-family:"Fira Sans",sans-serif;font-weight:600;font-size:86px;line-height:.9}

/* about */
.about{left:414px;top:798px;width:690px}
.about .kicker{font-family:"Fira Sans",sans-serif;font-weight:500;font-size:29px;display:flex;align-items:center;gap:8px;margin-left:3px}
.about .kicker .rule{width:44px}
.about .big{font-size:54px;margin-top:2px}
.about .lead{font-weight:600;font-size:15px;margin-top:30px}
.about p.body{font-size:12.5px;line-height:18.7px;color:var(--muted);margin-top:10px}
.about p.body+p.body{margin-top:10px}

/* services */
.section-title{font-size:54px;display:flex;align-items:center;gap:10px}
.section-title .rule{width:43px}
.services-title{left:0;width:1200px;top:1386px;justify-content:center}
.card{width:186px}
.card .thumb{width:186px;height:139px;display:block}
.card h3{font-family:"Source Sans 3",sans-serif;font-weight:600;font-size:17px;margin-top:18px;line-height:1.2}
.card p{font-size:11.5px;line-height:16.5px;color:var(--muted);margin-top:4px;padding-right:10px}

/* news */
.news-title{left:94px;top:2012px}
.post{width:232px}
.post .thumb{width:232px;height:153px;display:block}
.post .date{position:absolute;left:12px;top:141px;background:var(--green);color:var(--white);font-size:10.5px;font-weight:700;height:22px;padding:0 8px;display:flex;align-items:center;gap:6px;border-radius:6px 6px 0 0}
.post .date svg{display:block}
.post h3{font-family:"Source Sans 3",sans-serif;font-weight:600;font-size:17px;margin-top:22px;line-height:1.2}
.post p{font-size:11.5px;line-height:16.5px;color:var(--muted);margin-top:4px}

/* contact */
.contact-box{left:193px;top:2464px;width:814px;height:382px;background:var(--blue)}
.contact-box h2{font-family:"Fira Sans",sans-serif;font-weight:600;font-size:54px;color:var(--white);text-align:center;margin-top:42px;line-height:1}
.field{position:absolute;border:1px solid rgba(255,255,255,.75);color:var(--white);font-size:13px;display:flex;align-items:center;gap:6px;padding-left:9px}
.field.area{align-items:flex-start;padding-top:14px}
.send{position:absolute;left:355px;top:303px;width:121px;height:40px;background:var(--green);color:var(--white);font-weight:700;font-size:14px;display:flex;align-items:center;justify-content:center;gap:8px;letter-spacing:.3px}
.send .rule{width:16px;background:var(--white)}
.reach{top:2887px;color:var(--white);font-size:18px;font-weight:600;display:flex;align-items:center;gap:7px}
.reach .ring{width:44px;height:44px;border-radius:50%;border:1.5px solid rgba(255,255,255,.8);display:flex;align-items:center;justify-content:center}
.social{top:2982px;width:50px;height:50px;background:var(--green);border:2px solid #1c9a4c;border-radius:4px 18px 4px 18px}
.footer-line{left:0;top:3073px;width:1200px;height:1px;background:#444}
.copyright{left:0;width:1200px;top:3090px;text-align:center;font-size:11.5px;color:#8a8a8a}
.copyright b{color:var(--white);font-weight:600}
</style>
</head>
<body>
<div class="page">

  <!-- background shapes -->
  <svg class="abs" style="left:0;top:0" width="1200" height="3129" viewBox="0 0 1200 3129" aria-hidden="true">
    <polygon points="0,1230 1200,1230 1200,1913 565,1858 0,1858" fill="#f0eced"/>
    <polygon points="638,1281 1200,1230 1200,1340" fill="#27358f"/>
    <polygon points="0,1804 565,1858 0,1915" fill="#27358f"/>
    <polygon points="0,2611 1200,2715 1200,3129 0,3129" fill="#2a2a2a"/>
  </svg>

  <!-- hero photo -->
  <svg class="abs" style="left:0;top:94px" width="1200" height="650" viewBox="0 94 1200 650" role="img" aria-label="Photo: a smiling therapist with a notepad talking with a young girl on a sofa">
    <defs>
      <linearGradient id="heroTone" x1="0" y1="0" x2="1" y2="0">
        <stop offset="0" stop-color="#d9d6d3"/>
        <stop offset=".35" stop-color="#bdb6b0"/>
        <stop offset=".6" stop-color="#8f8d8b"/>
        <stop offset="1" stop-color="#e1cfc4"/>
      </linearGradient>
      <clipPath id="heroClip"><polygon points="0,94 1200,94 1200,743 0,640"/></clipPath>
    </defs>
    <g clip-path="url(#heroClip)">
      <rect x="0" y="94" width="1200" height="650" fill="url(#heroTone)"/>
      <circle cx="868" cy="729" r="264" fill="#3cae67"/>
      <circle cx="880" cy="729" r="256" fill="#1b7a3d"/>
    </g>
    <circle cx="119" cy="392" r="25" fill="none" stroke="#fff" stroke-width="2"/>
    <polyline points="124,381 113,392 124,403" fill="none" stroke="#fff" stroke-width="2"/>
    <circle cx="1080" cy="392" r="25" fill="none" stroke="#fff" stroke-width="2"/>
    <polyline points="1075,381 1086,392 1075,403" fill="none" stroke="#fff" stroke-width="2"/>
  </svg>

  <!-- header -->
  <div class="abs topbar">
    <span><svg width="10" height="13" viewBox="0 0 10 13"><path d="M5 0a5 5 0 0 1 5 5c0 3.5-5 8-5 8S0 8.5 0 5a5 5 0 0 1 5-5z" fill="#3cae67"/><circle cx="5" cy="5" r="2" fill="#27358f"/></svg>12 Lysveien, since 2000</span>
    <span><svg width="14" height="10" viewBox="0 0 14 10"><rect width="14" height="10" fill="#3cae67"/><polyline points="0,0 7,6 14,0" fill="none" stroke="#27358f" stroke-width="1.2"/></svg>info@fjordlysogsamhold.com</span>
  </div>
  <div class="abs brand"><i></i>FJORDLYS OG SAMHOLD</div>
  <nav class="abs nav">
    <a style="left:0">Om Fjordlys og Samhold</a>
    <a style="left:167px">Tjenester</a>
    <a style="left:264px">Aktuelt</a>
    <a style="left:351px">Kontakt</a>
  </nav>
  <div class="abs header-line"></div>

  <div class="abs hero-title">
    <div class="kicker"><span class="rule"></span>Norwegian</div>
    <div class="line1">Psychologist</div>
    <div class="line2">Service</div>
  </div>

  <!-- about photo -->
  <svg class="abs" style="left:0;top:650px" width="370" height="575" viewBox="0 650 370 575" role="img" aria-label="Photo: a happy girl jumping on a lawn in a park">
    <defs>
      <linearGradient id="aboutTone" x1="0" y1="0" x2="0" y2="1">
        <stop offset="0" stop-color="#c9cfd4"/>
        <stop offset=".5" stop-color="#9fb07f"/>
        <stop offset="1" stop-color="#5f8a3c"/>
      </linearGradient>
    </defs>
    <path d="M0,656 C200,740 361,830 361,947 C361,1070 180,1160 0,1215 Z" fill="url(#aboutTone)"/>
    <path d="M0,656 C200,740 361,830 361,947" fill="none" stroke="#27358f" stroke-width="4"/>
    <path d="M361,947 C361,1070 180,1160 0,1215" fill="none" stroke="#0f6e36" stroke-width="4"/>
  </svg>

  <div class="abs" style="left:1050px;top:750px;width:150px;height:300px;border-radius:50% 0 0 50%;background:radial-gradient(ellipse at 70% 50%,#ececec,rgba(255,255,255,0) 70%)" role="img" aria-label="Faint leaf decoration"></div>

  <section class="abs about">
    <div class="kicker"><span class="rule"></span>Om Fjordlys</div>
    <h1 class="heading big">Og Samhold</h1>
    <p class="lead">Lorem ipsum dolor sit amet, consectetur adipiscing elit. Integer ac tortor erat.</p>
    <p class="body">Duis vel nisi tristique, dignissim eros sit amet, iaculis leo. Maecenas ullamcorper mollis dolor a pulvinar. Aliquam a sem non dui tempus scelerisque id nec dolor. Quisque tincidunt at neque sit amet tempus. Curabitur nec porta velit, ut blandit libero. Aenean in augue non diam fringilla volutpat quis quis neque. Sed diam tortor, dapibus vitae dui eget, fermentum tincidunt ex. Etiam et libero fringilla, interdum tortor vitae, vehicula lacus. Vivamus tempus maximus neque sed consequat.</p>
    <p class="body">Cras egestas turpis vitae tortor scelerisque semper. Nullam rhoncus magna sit amet elit interdum auctor vel non sapien. Vivamus porttitor nulla in diam tristique, vitae facilisis nunc imperdiet. Suspendisse volutpat pretium ipsum ac tempor. Nullam non mauris lorem. Integer viverra, purus nec pellentesque porta, nisl nunc pulvinar urna, euismod suscipit ex quam consectetur velit. Maecenas et posuere sem. Curabitur elementum ullamcorper vulputate. Vestibulum sed molestie tellus.</p>
  </section>

  <!-- services -->
  <h2 class="abs heading section-title services-title"><span class="rule"></span>Tjenester<span class="rule"></span></h2>

  <div class="abs" style="left:1100px;top:1660px;width:100px;height:240px;background:radial-gradient(ellipse at 80% 50%,#e2dedf,rgba(240,236,237,0) 70%)" role="img" aria-label="Faint leaf decoration"></div>

  <article class="abs card" style="left:94px;top:1489px">
    <svg class="thumb" viewBox="0 0 186 139" role="img" aria-label="Photo: psychologist holding a folder in a bright office"><path d="M0 0H166Q186 0 186 20V139H0Z" fill="#c8c2b8"/><path d="M184 18V137H0" fill="none" stroke="#0f6e36" stroke-width="3"/></svg>
    <h3>Utredning</h3>
    <p>Cras egestas turpis vitae tortor sceleue semper. Nullam rhoncus magna sit amet elit interdum auctor vel non sapien. Vivamus porttitor nulla in diam</p>
  </article>
  <article class="abs card" style="left:300px;top:1489px">
    <svg class="thumb" viewBox="0 0 186 139" role="img" aria-label="Photo: counselling conversation between two adults"><path d="M0 0H166Q186 0 186 20V139H0Z" fill="#b9b2a8"/><path d="M184 18V137H0" fill="none" stroke="#0f6e36" stroke-width="3"/></svg>
    <h3>Rådgivning</h3>
    <p>Cras egestas turpis vitae tortor sceleue semper. Nullam rhoncus magna sit amet elit interdum auctor vel non sapien. Vivamus porttitor nulla in diam</p>
  </article>
  <article class="abs card" style="left:506px;top:1489px">
    <svg class="thumb" viewBox="0 0 186 139" role="img" aria-label="Photo: participants seated at a workshop"><path d="M0 0H166Q186 0 186 20V139H0Z" fill="#8c8580"/><path d="M184 18V137H0" fill="none" stroke="#0f6e36" stroke-width="3"/></svg>
    <h3>Kurs og work shops</h3>
    <p>Cras egestas turpis vitae tortor sceleue semper. Nullam rhoncus magna sit amet elit interdum auctor vel non sapien. Vivamus porttitor nulla in diam</p>
  </article>
  <article class="abs card" style="left:713px;top:1489px">
    <svg class="thumb" viewBox="0 0 186 139" role="img" aria-label="Photo: therapist's hands during a treatment session"><path d="M0 0H166Q186 0 186 20V139H0Z" fill="#7f9cc4"/><path d="M184 18V137H0" fill="none" stroke="#0f6e36" stroke-width="3"/></svg>
    <h3>Terapi og utvikling</h3>
    <p>Cras egestas turpis vitae tortor sceleue semper. Nullam rhoncus magna sit amet elit interdum auctor vel non sapien. Vivamus porttitor nulla in diam</p>
  </article>
  <article class="abs card" style="left:919px;top:1489px">
    <svg class="thumb" viewBox="0 0 186 139" role="img" aria-label="Photo: hands joining two puzzle pieces about self development"><path d="M0 0H166Q186 0 186 20V139H0Z" fill="#8e7461"/><path d="M184 18V137H0" fill="none" stroke="#0f6e36" stroke-width="3"/></svg>
    <h3>Lorem ipsum</h3>
    <p>Cras egestas turpis vitae tortor sceleue semper. Nullam rhoncus magna sit amet elit interdum auctor vel non sapien. Vivamus porttitor nulla in diam</p>
  </article>

  <!-- news -->
  <div class="abs" style="left:0;top:2130px;width:90px;height:320px;background:radial-gradient(ellipse at 20% 50%,#e8e8e8,rgba(255,255,255,0) 70%)" role="img" aria-label="Faint leaf decoration"></div>

  <h2 class="abs heading section-title news-title"><span class="rule"></span>Aktuelt</h2>

  <article class="abs post" style="left:94px;top:2083px">
    <svg class="thumb" viewBox="0 0 232 153" role="img" aria-label="Photo: therapist's hands on a patient's back"><rect width="232" height="153" fill="#a9b3b8"/></svg>
    <div class="date"><svg width="11" height="11" viewBox="0 0 11 11"><rect x=".5" y="1.5" width="10" height="9" fill="none" stroke="#fff"/><line x1="0" y1="4" x2="11" y2="4" stroke="#fff"/></svg>| Jan. 10, 2020</div>
    <h3>Lorem ipsum</h3>
    <p>Praesent ac convallis ex. Integer ac tortor erat. Duis vel nisi tristique, dignissim eros sit amet, iaculis leo. Maecenas ullamcorper mollis dolor a pulvinar.</p>
  </article>
  <article class="abs post" style="left:344px;top:2083px">
    <svg class="thumb" viewBox="0 0 232 153" role="img" aria-label="Photo: a hand stacking wooden blocks into a pyramid"><rect width="232" height="153" fill="#d8cbb9"/></svg>
    <div class="date"><svg width="11" height="11" viewBox="0 0 11 11"><rect x=".5" y="1.5" width="10" height="9" fill="none" stroke="#fff"/><line x1="0" y1="4" x2="11" y2="4" stroke="#fff"/></svg>| Jan. 10, 2020</div>
    <h3>Lorem ipsum</h3>
    <p>Praesent ac convallis ex. Integer ac tortor erat. Duis vel nisi tristique, dignissim eros sit amet, iaculis leo. Maecenas ullamcorper mollis dolor a pulvinar.</p>
  </article>
  <article class="abs post" style="left:594px;top:2083px">
    <svg class="thumb" viewBox="0 0 232 153" role="img" aria-label="Photo: physiotherapist treating a leg"><rect width="232" height="153" fill="#c7a995"/><rect y="118" width="232" height="35" fill="#3f52b8"/></svg>
    <div class="date"><svg width="11" height="11" viewBox="0 0 11 11"><rect x=".5" y="1.5" width="10" height="9" fill="none" stroke="#fff"/><line x1="0" y1="4" x2="11" y2="4" stroke="#fff"/></svg>| Jan. 10, 2020</div>
    <h3>Lorem ipsum</h3>
    <p>Praesent ac convallis ex. Integer ac tortor erat. Duis vel nisi tristique, dignissim eros sit amet, iaculis leo. Maecenas ullamcorper mollis dolor a pulvinar.</p>
  </article>

  <svg class="abs" style="left:850px;top:1925px" width="350" height="565" viewBox="850 1925 350 565" role="img" aria-label="Photo: a client and a therapist talking in chairs">
    <path d="M1200,1931 C1000,2040 856,2110 856,2211 C856,2320 1020,2400 1200,2484 Z" fill="#e6e4e6"/>
    <path d="M1200,1931 C1000,2040 856,2110 856,2211" fill="none" stroke="#27358f" stroke-width="4"/>
    <path d="M856,2211 C856,2320 1020,2400 1200,2484" fill="none" stroke="#0f6e36" stroke-width="4"/>
  </svg>

  <!-- contact -->
  <section class="abs contact-box">
    <h2>Kontakt</h2>
    <div class="field" style="left:32px;top:121px;width:246px;height:40px">
      <svg width="13" height="13" viewBox="0 0 13 13"><circle cx="6.5" cy="4" r="3" fill="none" stroke="#fff"/><path d="M1 13c0-3 2.5-5 5.5-5s5.5 2 5.5 5" fill="none" stroke="#fff"/></svg>Ditt navn</div>
    <div class="field" style="left:284px;top:121px;width:248px;height:40px">
      <svg width="15" height="11" viewBox="0 0 15 11"><rect x=".5" y=".5" width="14" height="10" fill="none" stroke="#fff"/><polyline points=".5,.5 7.5,6 14.5,.5" fill="none" stroke="#fff"/></svg>E-post</div>
    <div class="field" style="left:537px;top:121px;width:248px;height:40px">
      <svg width="13" height="13" viewBox="0 0 13 13"><rect x=".5" y="2.5" width="10" height="10" fill="none" stroke="#fff"/><line x1="5" y1="8" x2="12.5" y2=".5" stroke="#fff" stroke-width="1.5"/></svg>Emne</div>
    <div class="field area" style="left:32px;top:166px;width:753px;height:121px">
      <svg width="14" height="13" viewBox="0 0 14 13"><rect x=".5" y=".5" width="13" height="10" rx="1" fill="none" stroke="#fff"/><line x1="3" y1="4" x2="11" y2="4" stroke="#fff"/><line x1="3" y1="7" x2="9" y2="7" stroke="#fff"/></svg>Melding</div>
    <div class="send"><span class="rule"></span>SEND NOW</div>
  </section>

  <div class="abs reach" style="left:362px">
    <span class="ring"><svg width="18" height="13" viewBox="0 0 18 13"><rect x=".5" y=".5" width="17" height="12" fill="#fff"/><polyline points=".5,.5 9,7 17.5,.5" fill="none" stroke="#2a2a2a" stroke-width="1.2"/></svg></span>Info@fjordlysogsamhold.com
  </div>
  <div class="abs reach" style="left:654px">
    <span class="ring"><svg width="18" height="18" viewBox="0 0 24 24"><path d="M6.6 10.8a15 15 0 0 0 6.6 6.6l2.2-2.2a1 1 0 0 1 1-.25 11.4 11.4 0 0 0 3.6.57 1 1 0 0 1 1 1V20a1 1 0 0 1-1 1A17 17 0 0 1 3 4a1 1 0 0 1 1-1h3.5a1 1 0 0 1 1 1c0 1.25.2 2.45.57 3.57a1 1 0 0 1-.25 1z" fill="#fff"/></svg></span>01-234-567-8900
  </div>

  <a class="abs social" style="left:516px" aria-label="Social profile 1"></a>
  <a class="abs social" style="left:576px" aria-label="Social profile 2"></a>
  <a class="abs social" style="left:635px" aria-label="Social profile 3"></a>

  <div class="abs footer-line"></div>
  <p class="abs copyright">© 2020 <b>Fjordlys og samhold.</b> All Right Reserved</p>
</div>
</body>
</html>
```